Hardcore nerd needs to stand out in a sea of dull Defence business cards

Wombat Devices is a new Australian consulting engineering company that turns research and theory into practical systems. No evangelistic fluff, just mathematics and physics into electronic and optical circuits for consumer products, scientific research or Defence applications.

We already have a recognised logo (provided) which is often dark blue/black on a light background but we're open to other combinations. (Us engineers tend to have limited aesthetic imagination :)

Some of our recent products have included:
* Instrumentation for electrical testing,
* Radar jammers,
* GPS antenna design,
* Satellite tracking systems,
* High power lasers

We're open to both single and double-sided designs - happy to be convinced either way.

P.S. Another group is working on the web page, so - alas - our web site is currently of no use for images/ideas...

Target Market(s)

Engineering managers,
Scientists

Contact Information for Business Card

Dr Colin Marsh
R&D Engineer

colin@wombatdevicesco.com.au
0427 563 210

PO Box XXX (to be confirmed)
Banks ACT 2913
Australia

Font styles to use
Serif
Sans Serif

Colors

Designer to choose colors to be used in the design.

Requirements
Must have
• My contact details!
• I've had many (great) "bold and plain" designs submitted already, so feel free to be artistically creative :)
• Happy to take advice re fonts/colours/printability etc.
Nice to have
• I'm not sure if "lists" are more at home on a CV than a business card, but representative services include:
• Applied electromagnetics
• RF and high speed electronics
• Signal and image processing
• Electro-optical and laser systems
• Concept-to-prototype design services
• If you're considering double sided cards, then often measuring/alignment grids/rulers feature on the back of similar cards.
• e.g. https://www.lumoptix-example.com/newgrouppage9.cfm?objectgroup_id=4815
• https://www.lumoptix-example.com/newgrouppage9.cfm?objectgroup_ID=4817
• ..or even a "Smith chart" (google will return lots)
• Generic images to represent a capability might work - googling images associated with keyword for each of these areas might help:
• - "passive radar", "phased array", "fdtd", "vircator"
• RF and high speed electronic design
• - "smith chart", "microstrip circuits", "dimensioned drawing", "electronic schematic"
• - "dft", "iir filter"
• - "optical cavity". "laser energy level diagram"
• Background/watermarked images outlines/wireframes/schematics would probably look OK.
Should not have
• If a list of projects/services is provided, it is important not to make the client feel that this is "all" the company can do. Engineering design is a creative discipline (like graphics :)
• Please, no stock "military" snaps like planes, missiles, etc!

```html
<!DOCTYPE html>
<html lang="en">
<head>
<meta charset="utf-8">
<title>Wombat Devices – Business Card</title>
<link rel="stylesheet" href="https://fonts.googleapis.com/css2?family=Lato:wght@400;700;900&display=swap">
<style>
  :root {
    --navy: #0b2466;
    --navy-soft: #12307a;
    --paper: #f3f3f3;
    --ink: #2b2b2b;
    --stage: #e4e5e8;
    --rule: #dcdcdc;
  }
  * { margin: 0; padding: 0; box-sizing: border-box; }
  html, body {
    width: 1200px; height: 1015px; overflow: hidden;
    background: var(--stage);
    font-family: "Lato", Arial, sans-serif;
  }
  .stage {
    position: relative; width: 1200px; height: 1015px;
  }
  .card {
    position: absolute; left: 220px; width: 760px; height: 434px;
    box-shadow: 0 6px 18px rgba(0,0,0,0.18);
    overflow: hidden;
  }
  /* Front */
  .card-front { top: 48px; background: var(--navy); }
  .front-ring {
    position: absolute; left: 230px; top: 67px; width: 300px; height: 300px;
    border-radius: 50%; border: 34px solid var(--navy-soft);
  }
  .front-wordmark {
    position: absolute; inset: 0;
    display: flex; flex-direction: column; align-items: center; justify-content: center;
    color: #fff; font-weight: 900; line-height: 1;
  }
  .front-wordmark span { font-size: 54px; letter-spacing: 3px; }
  .front-wordmark span + span { margin-top: 10px; font-size: 54px; }
  /* Back */
  .card-back { top: 530px; background: var(--paper); }
  .back-band {
    position: absolute; left: 0; right: 0; bottom: 0; height: 16px; background: var(--navy);
  }
  .back-logo {
    position: absolute; left: 52px; top: 248px;
    display: flex; align-items: center; gap: 14px;
  }
  .back-logo-dot {
    width: 58px; height: 58px; border-radius: 50%; background: var(--navy); flex: none;
  }
  .back-logo-name {
    color: var(--navy); font-weight: 900; font-size: 25px; line-height: 1.05; letter-spacing: 1px;
  }
  .back-divider {
    position: absolute; left: 330px; top: 40px; width: 1px; height: 230px; background: var(--rule);
  }
  .contact {
    position: absolute; left: 362px; top: 62px; color: var(--ink);
  }
  .contact-name {
    color: var(--navy); font-weight: 900; font-size: 22px; letter-spacing: 0.3px;
  }
  .contact-role { font-size: 17px; margin-top: 2px; }
  .contact-lines { list-style: none; margin-top: 14px; }
  .contact-lines li {
    display: flex; align-items: center; gap: 10px; font-size: 18px; line-height: 1.45;
  }
  .contact-lines svg { width: 14px; height: 14px; fill: var(--navy); flex: none; }
  .contact-address { margin-top: 14px; font-size: 18px; line-height: 1.4; }
</style>
</head>
<body>
<main class="stage">
  <section class="card card-front" aria-label="Card front">
    <div class="front-ring" aria-hidden="true"></div>
    <div class="front-wordmark"><span>WOMBAT</span><span>DEVICES</span></div>
  </section>

  <section class="card card-back" aria-label="Card back">
    <div class="back-logo">
      <div class="back-logo-dot" aria-hidden="true"></div>
      <div class="back-logo-name">WOMBAT<br>DEVICES</div>
    </div>
    <div class="back-divider" aria-hidden="true"></div>
    <div class="contact">
      <div class="contact-name">DR COLIN MARSH</div>
      <div class="contact-role">R&amp;D Engineer</div>
      <ul class="contact-lines">
        <li>
          <svg viewBox="0 0 16 16" aria-hidden="true"><path d="M3 1h3l1.5 4-2 1.3a9 9 0 0 0 4.2 4.2L11 8.5l4 1.5v3a2 2 0 0 1-2 2A12 12 0 0 1 1 3a2 2 0 0 1 2-2z"/></svg>
          0427 563 210
        </li>
        <li>
          <svg viewBox="0 0 16 16" aria-hidden="true"><path d="M1 3h14v10H1z M2 4l6 5 6-5" fill="var(--navy)" stroke="#fff" stroke-width="1.2"/></svg>
          colin@wombatdevicesco.com.au
        </li>
        <li>
          <svg viewBox="0 0 16 16" aria-hidden="true"><circle cx="8" cy="8" r="7"/><path d="M1 8h14M8 1c-3 4-3 10 0 14M8 1c3 4 3 10 0 14" fill="none" stroke="#fff" stroke-width="1"/></svg>
          www.wombatdevicesco.com.au
        </li>
      </ul>
      <div class="contact-address">PO Box XXX<br>Banks ACT 2913, Australia</div>
    </div>
    <div class="back-band" aria-hidden="true"></div>
  </section>
</main>
</body>
</html>
```